Website Redesign for Mortgage, Property and Conveyancing business

Project Overview:
We are looking for a refresh and redesign of our current website to a smart, crisp and fresh approach to Home Loans, Conveyancing and Property sales. This task will be to:
- Redesign our current website in accordance with the new wireframe.
- Provide all elements required for the design
- Build 7 key templates including:
Home Page
2nd Level Section Page
3rd level Product landing Page
2nd Level - About Us, Contact Us etc
Blog
Blog Article
Campaign Page - no header
Technical
The design is for a Wordpress website. Existing theme is Quartzline and we use Elementor for page editing. We are open to a new theme to be introduced but would prefer to stay with elementor.
Current Site is: www.bluecanopy.com.au
Sites that we like or elements of sites:
Marlow Real Estate: https://www.marlow.com.au/ (Like use of video and navigation)
Copper Lantern Way - Mortage: https://clw.com.au/refinance-home-loan/ (Like landing pages a sin example)
Fernwick: https://fernwick.com.au/ (like Our services section).
Industry/Entity Type
Mortgage, Property, Conveyancing, Property Investment
Coding
Coded - Design and coding required
Number of Pages Required
5+ page
Requirements
Must have
- Built for Wordpress and Elementor.
Nice to have
- See Project Description for links to ideas/elements that we have liked. However, open to ideas as long as the follow the navigation set out in the wire frame.

```html
<!DOCTYPE html>
<html lang="en">
<head>
<meta charset="utf-8">
<title>Brightfield Group Services</title>
<link href="https://fonts.googleapis.com/css2?family=EB+Garamond:wght@600;700&family=Poppins:ital,wght@0,400;0,500;1,500&display=swap" rel="stylesheet">
<style>
:root{
  --green:#0ca54b;
  --green-head:#14a04a;
  --green-deep:#1b7b3e;
  --navy:#0c2a66;
  --grey-bg:#f4f4f4;
  --text:#555;
  --white:#fff;
}
*{box-sizing:border-box;margin:0;padding:0}
html,body{width:1200px;height:3816px;overflow:hidden}
body{font-family:"Poppins",sans-serif;color:var(--text);background:var(--white);position:relative}
.abs{position:absolute}
.serif{font-family:"EB Garamond",serif;font-weight:700;color:var(--green-head);text-align:center;line-height:1.02}
/* header */
.site-header{top:0;left:0;width:1200px;height:120px;background:var(--white)}
.brand{left:86px;top:32px;display:flex;align-items:center;gap:12px}
.brand-mark{width:50px;height:50px;border-radius:50%;background:var(--navy)}
.brand-name{font-size:26px;font-weight:500;color:var(--navy);line-height:1}
.brand-name small{display:block;font-size:12px;letter-spacing:3px;margin-top:4px}
.main-nav{left:423px;top:50px;display:flex;gap:21px;font-size:15px;color:#666}
.main-nav .active{color:var(--navy);font-weight:500}
.btn{display:flex;align-items:center;justify-content:center;font-size:16px}
.btn-solid{background:var(--green);color:var(--white)}
.btn-outline{border:2px solid var(--navy);color:var(--navy);background:var(--white)}
.header-cta{left:971px;top:38px;width:144px;height:42px}
/* hero */
.hero-bg{top:120px;left:0;width:1200px;height:380px;background:var(--grey-bg)}
.hero-title{top:160px;left:0;width:1200px;font-size:62px}
.lead{font-size:15px;text-align:center;line-height:24px;color:#555}
.hero-lead{top:300px;left:190px;width:820px}
.hero-read{left:428px;top:367px;width:163px;height:47px}
.hero-contact{left:607px;top:367px;width:165px;height:47px}
.strip{top:370px;left:0}
.panel-text{top:575px;left:302px;width:294px;text-align:center;color:var(--white)}
.panel-text h3{font-weight:500;font-size:20px;margin-bottom:14px}
.panel-text p{font-size:15px;line-height:24px}
.panel-arrow{margin:18px auto 0;width:46px;height:46px;border:2px solid var(--white);border-radius:50%;display:flex;align-items:center;justify-content:center}
.trusted-title{top:948px;left:0;width:1200px;font-size:62px}
/* video */
.video-band{top:1290px;left:0;width:1200px;height:372px;background:var(--grey-bg)}
.video{top:1116px;left:84px;width:1033px;height:489px;background:linear-gradient(135deg,#d8d3cc,#b89468 45%,#8c7a66 70%,#e4e2de)}
.play{top:1320px;left:560px;width:80px;height:80px;border-radius:50%;background:var(--white);border:3px dotted var(--green);display:flex;align-items:center;justify-content:center}
/* services */
.services-title{top:1705px;left:0;width:1200px;font-size:62px}
.services-lead{top:1782px;left:190px;width:820px}
.service-label{font-size:17px;color:var(--green);text-transform:uppercase;line-height:24px}
.service-icon{width:52px;height:52px;border-radius:50%;background:var(--navy);border:3px double var(--white);box-shadow:0 0 0 2px var(--navy);display:flex;align-items:center;justify-content:center}
.hub{top:2050px;left:460px;width:240px;height:240px;border-radius:50%;background:radial-gradient(circle at 40% 35%,#fff,#e9f3ec);box-shadow:0 10px 24px rgba(0,0,0,.12);display:flex;align-items:center;justify-content:center;font-size:22px;font-weight:500;color:var(--navy)}
/* band */
.promo{top:2418px;left:0;width:1200px;height:315px;background:linear-gradient(90deg,var(--green-deep),#2a8a4c 40%,#1f7d40)}
.promo-title{top:2470px;left:0;width:1200px;font-size:60px;color:var(--white)}
.promo-lead{top:2550px;left:230px;width:740px;color:var(--white)}
.promo-btn{top:2633px;left:560px;width:167px;height:42px;border:1px solid var(--white);color:var(--white);font-size:15px}
/* testimonials */
.reviews-title{top:2808px;left:0;width:1200px;font-size:62px}
.review{top:2920px;width:327px;height:262px;background:#f7f7f7;box-shadow:0 2px 6px rgba(0,0,0,.06);text-align:center;padding-top:16px}
.avatar{width:70px;height:70px;border-radius:50%;margin:0 auto;background:linear-gradient(#b88c70,#6a4a3a)}
.stars{color:#f2b01e;font-size:14px;letter-spacing:1px;margin-top:8px}
.review h4{font-weight:400;font-size:17px;color:#333}
.review em{font-size:14px;font-weight:500;color:var(--green)}
.review p{font-size:13.5px;line-height:21px;margin:10px 18px 0;color:#666}
.arrow-btn{top:3206px;width:46px;height:46px;border:2px solid var(--navy);border-radius:50%;display:flex;align-items:center;justify-content:center}
/* footer */
.footer{top:3307px;left:0;width:1200px;height:393px;background:var(--green);color:var(--white)}
.foot-col{top:3390px}
.foot-col h5{font-weight:400;font-size:20px;padding-bottom:10px;position:relative}
.foot-col h5::after{content:"";position:absolute;left:0;bottom:0;width:40px;height:2px;background:var(--white)}
.foot-col ul{list-style:none;margin-top:30px;font-size:15px}
.foot-col li{height:31px}
.foot-col li::before{content:"›";margin:0 12px 0 6px;font-size:18px}
.contact-item{display:flex;gap:20px;margin-top:22px;font-size:15px;line-height:20px}
.contact-item:first-of-type{margin-top:30px}
.contact-icon{width:32px;height:32px;border:2px solid var(--white);border-radius:4px;flex:none;display:flex;align-items:center;justify-content:center}
.bottom-bar{top:3700px;left:0;width:1200px;height:116px;background:var(--navy);color:var(--white)}
.socials{top:3735px;left:89px;display:flex;gap:9px}
.socials span{width:42px;height:42px;border:2px solid var(--white);border-radius:50%}
.copyright{top:3748px;right:90px;font-size:15px;color:var(--white)}
</style>
</head>
<body>

<header class="site-header abs">
  <div class="brand abs"><span class="brand-mark"></span><span class="brand-name">Brightfield<small>GROUP SERVICES</small></span></div>
  <nav class="main-nav abs"><span class="active">Home</span><span>Services</span><span>Why Choose Us</span><span>About</span><span>Blog</span><span>Testimonials</span></nav>
  <a class="btn btn-solid header-cta abs">Contact Us</a>
</header>

<section class="hero">
  <div class="hero-bg abs"></div>
  <h1 class="serif hero-title abs">We’re here to help you increase your<br>financial wellbeing</h1>
  <p class="lead hero-lead abs">We’ve been in business for over 20 years. Brightfield Group Services is the all-in-one answer to reaching your property and financial goals more easily.</p>
  <a class="btn btn-solid hero-read abs">Read More</a>
  <a class="btn btn-outline hero-contact abs">Contact Us</a>

  <svg class="strip abs" width="1200" height="580" viewBox="0 0 1200 580">
    <defs>
      <clipPath id="waveClip"><path d="M0 10 Q600 170 1200 10 L1200 570 Q600 440 0 570 Z"/></clipPath>
      <linearGradient id="keys" x1="0" y1="0" x2="1" y2="1"><stop offset="0" stop-color="#ddd3c6"/><stop offset="1" stop-color="#b59a6a"/></linearGradient>
      <linearGradient id="worry" x1="0" y1="0" x2="1" y2="1"><stop offset="0" stop-color="#3a3a3a"/><stop offset="1" stop-color="#b8b8b8"/></linearGradient>
      <linearGradient id="family" x1="0" y1="0" x2="1" y2="1"><stop offset="0" stop-color="#cfc6b8"/><stop offset="1" stop-color="#7fb3a3"/></linearGradient>
    </defs>
    <g clip-path="url(#waveClip)">
      <rect x="0" y="0" width="298" height="580" fill="url(#keys)" role="img" aria-label="Hand holding house keys in front of a model home"/>
      <rect x="300" y="0" width="297" height="580" fill="#2f8a4c"/>
      <rect x="599" y="0" width="294" height="580" fill="url(#worry)" role="img" aria-label="Man reviewing bills and coins at a desk"/>
      <rect x="895" y="0" width="305" height="580" fill="url(#family)" role="img" aria-label="Mother lifting a happy toddler"/>
    </g>
  </svg>
  <div class="panel-text abs">
    <h3>PROPERTY INVERSTMENT</h3>
    <p>Integrated finance, conveyancing, property investment and property management along with accounting solutions.</p>
    <div class="panel-arrow"><svg width="14" height="14" viewBox="0 0 14 14"><path d="M5 2l5 5-5 5" stroke="#fff" stroke-width="2" fill="none"/></svg></div>
  </div>
</section>

<h2 class="serif trusted-title abs">A trusted team for your property and<br>home loan journey.</h2>

<section class="video-section">
  <div class="video-band abs"></div>
  <div class="video abs" role="img" aria-label="Family unpacking moving boxes in a new home"></div>
  <div class="play abs"><svg width="30" height="32" viewBox="0 0 30 32"><path d="M3 2l25 14L3 30z" fill="var(--green)"/></svg></div>
</section>

<section class="services">
  <h2 class="serif services-title abs">Our Services</h2>
  <p class="lead services-lead abs">We’ve been in business for over 20 years. Brightfield Group Services is the all-in-one answer to reaching your property and financial goals more easily.</p>
  <svg class="abs" style="top:1990px;left:400px" width="360" height="360" viewBox="0 0 360 360">
    <circle cx="180" cy="180" r="150" fill="none" stroke="var(--green)" stroke-width="1.2" stroke-dasharray="2 4"/>
    <g fill="#fff" stroke="var(--green)" stroke-width="1.2">
      <circle cx="180" cy="29" r="8"/><circle cx="73" cy="71" r="8"/><circle cx="288" cy="71" r="8"/><circle cx="30" cy="180" r="8"/><circle cx="332" cy="180" r="8"/>
    </g>
  </svg>
  <div class="hub abs">Brightfield</div>

  <div class="service-label abs" style="top:1903px;left:480px;width:200px;text-align:center">Extensions</div>
  <div class="service-icon abs" style="top:1942px;left:554px"></div>
  <div class="service-label abs" style="top:2046px;left:120px;width:265px;text-align:right">Loft Conversions</div>
  <div class="service-icon abs" style="top:2032px;left:394px"></div>
  <div class="service-icon abs" style="top:2032px;left:714px"></div>
  <div class="service-label abs" style="top:2046px;left:774px">Electrical Work</div>
  <div class="service-label abs" style="top:2158px;left:80px;width:262px;text-align:right">Kitchen &amp; Bathroom<br>Installations</div>
  <div class="service-icon abs" style="top:2144px;left:352px"></div>
  <div class="service-icon abs" style="top:2144px;left:757px"></div>
  <div class="service-label abs" style="top:2158px;left:817px">Painting and Decorating</div>
</section>

<section>
  <div class="promo abs" role="img" aria-label="Smiling couple in a green tinted photograph"></div>
  <h2 class="serif promo-title abs">A trusted team for your property</h2>
  <p class="lead promo-lead abs" style="line-height:22px">Harbour Canvas Co not only carries the toughest boat cover brands on the market, but we also carry the widest selection of boat cover styles. We have universal boat covers that are applicable to many boat types</p>
  <a class="btn promo-btn abs">Shop Now</a>
</section>

<section class="reviews">
  <h2 class="serif reviews-title abs">What Our Client Says</h2>
  <article class="review abs" style="left:99px"><div class="avatar" role="img" aria-label="Client portrait"></div><div class="stars">★★★★★</div><h4>Harper Lane</h4><em>Organiser</em><p>We don't place you into a loan profile each customer as an formula created by the banking industry.</p></article>
  <article class="review abs" style="left:440px"><div class="avatar" role="img" aria-label="Client portrait" style="background:linear-gradient(#e3b23c,#555)"></div><div class="stars">★★★★★</div><h4>Harper Lane</h4><em>Organiser</em><p>We don't place you into a loan profile each customer as an formula created by the banking industry.</p></article>
  <article class="review abs" style="left:783px"><div class="avatar" role="img" aria-label="Client portrait" style="background:linear-gradient(#ddd,#7a4b38)"></div><div class="stars">★★★★★</div><h4>Harper Lane</h4><em>Organiser</em><p>We don't place you into a loan profile each customer as an formula created by the banking industry.</p></article>
  <div class="arrow-btn abs" style="left:539px"><svg width="12" height="12" viewBox="0 0 12 12"><path d="M8 1L3 6l5 5" stroke="var(--navy)" stroke-width="2" fill="none"/></svg></div>
  <div class="arrow-btn abs" style="left:608px"><svg width="12" height="12" viewBox="0 0 12 12"><path d="M4 1l5 5-5 5" stroke="var(--navy)" stroke-width="2" fill="none"/></svg></div>
</section>

<footer>
  <div class="footer abs"></div>
  <div class="foot-col abs" style="left:211px;color:#fff"><h5>Quick Links</h5><ul><li>Home</li><li>About Us</li><li>Our Services</li><li>Our Blogs</li><li>Testimonials</li></ul></div>
  <div class="foot-col abs" style="left:452px;color:#fff"><h5>What we Do</h5><ul><li>Fiance</li><li>Property Inversment</li><li>Property sales</li><li>Property amnagement</li><li>Conversing</li></ul></div>
  <div class="foot-col abs" style="left:762px;color:#fff"><h5>Contact Us</h5>
    <div class="contact-item"><span class="contact-icon"><svg width="14" height="14" viewBox="0 0 14 14"><path d="M3 1l3 3-2 2c1 2 2 3 4 4l2-2 3 3-2 2C6 13 1 8 1 3z" fill="#fff"/></svg></span><span>CALL US<br>(800) 555-0142</span></div>
    <div class="contact-item"><span class="contact-icon"><svg width="14" height="10" viewBox="0 0 14 10"><rect x="0.5" y="0.5" width="13" height="9" fill="none" stroke="#fff"/><path d="M1 1l6 5 6-5" stroke="#fff" fill="none"/></svg></span><span>EMAIL US<br>info@bluecanopy.com.au</span></div>
    <div class="contact-item"><span class="contact-icon"><svg width="12" height="16" viewBox="0 0 12 16"><path d="M6 1a5 5 0 015 5c0 4-5 9-5 9S1 10 1 6a5 5 0 015-5z" fill="#fff"/><circle cx="6" cy="6" r="2" fill="var(--green)"/></svg></span><span>24 Wattle Street, Glenhaven,<br>VIC 3199</span></div>
  </div>
  <div class="bottom-bar abs"></div>
  <div class="socials abs"><span aria-label="Video channel"></span><span aria-label="Social page"></span><span aria-label="Social feed"></span><span aria-label="Photo feed"></span></div>
  <p class="copyright abs">© 2024 Kestrel Pty Ltd - All Rights Reserved - ABN: 41 200 358 114</p>
</footer>

</body>
</html>
```